Financial Services Sales Sheet

We need this sheet redesigned. Needs to feel very corporate/financial. open to imagery/icons/colors/etc. Copy is in the docx file to expedite work. PDF is what client has done inh-house and feels dated.

```html
<!DOCTYPE html>
<html lang="en">
<head>
<meta charset="utf-8">
<title>Harbor Ledger Advisors – Sales Sheet</title>
<link rel="stylesheet" href="https://fonts.googleapis.com/css2?family=Montserrat:wght@400;500;600;700;800&display=swap">
<style>
:root{
  --navy:#0b3a78;
  --band:#1f5796;
  --tan:#c8b49e;
  --paper:#ffffff;
  --mist:#f3f3f4;
  --ink:#1b1b1f;
  --stage:#9d9d9d;
  --photo-a:#8a7566;
  --photo-b:#b9a797;
}
*{margin:0;padding:0;box-sizing:border-box}
html,body{width:729px;height:1200px;overflow:hidden}
body{background:var(--stage);font-family:"Montserrat",sans-serif;color:var(--ink);position:relative}
.sheet{position:absolute;left:157px;width:415px;height:585px;background:var(--paper);overflow:hidden}
.sheet--front{top:10px}
.sheet--back{top:605px}
.brand{position:absolute;left:33px;top:24px;display:flex;align-items:center;gap:6px}
.brand__dot{width:18px;height:18px;border-radius:50%;background:var(--navy)}
.brand__name{font-weight:800;font-size:9.5px;line-height:1;color:var(--navy);letter-spacing:.2px}
.brand__tag{position:absolute;left:24px;top:21px;font-size:4.6px;font-weight:500;color:var(--navy);white-space:nowrap;letter-spacing:.2px}
.url-pill{position:absolute;left:234px;top:36px;width:140px;height:18px;border-radius:9px;background:var(--tan);font-size:8.4px;font-weight:500;color:var(--ink);display:flex;align-items:center;justify-content:center}
.photo{position:absolute;background:linear-gradient(135deg,var(--photo-a),var(--photo-b) 60%,#d9d4cf)}
.photo--building{left:10px;top:84px;width:396px;height:253px}
.title-band{position:absolute;left:0;top:211px;width:286px;height:100px;background:var(--band);padding:12px 0 0 33px}
.title-band h1{color:#fff;font-weight:700;font-size:20.5px;line-height:26px;letter-spacing:.3px}
.subtitle{position:absolute;left:40px;top:360px;font-size:11px;font-weight:500;line-height:13.5px}
.intro{position:absolute;left:30px;top:398px;width:365px;height:52px;background:var(--mist);padding:7px 10px;font-size:7.3px;line-height:9.2px;font-weight:500}
.col{position:absolute;top:468px;width:180px}
.col--left{left:34px}
.col--right{left:205px}
.col h2{font-size:11px;font-weight:700;line-height:13px;border-left:1.5px solid var(--navy);padding-left:5px}
.checks{list-style:none;margin-top:10px}
.checks li{position:relative;padding-left:8px;font-size:6.2px;line-height:9.7px;font-weight:500}
.checks li::before{content:"";position:absolute;left:0;top:2.3px;width:5px;height:5px;border:.8px solid var(--navy);border-radius:50%}
.checks li::after{content:"";position:absolute;left:1.6px;top:3.6px;width:1.8px;height:1px;border-left:.8px solid var(--navy);border-bottom:.8px solid var(--navy);transform:rotate(-45deg)}
.checks--tight li{line-height:9.8px}

/* back */
.snapshot{position:absolute;left:222px;top:0;width:193px;height:284px;background:var(--navy);color:#fff;padding:34px 0 0 21px}
.snapshot h3{font-size:10.4px;font-weight:600;line-height:12.5px;letter-spacing:.3px}
.stat{width:150px;border-bottom:.6px solid rgba(255,255,255,.25);padding:13px 0 6px}
.stat:last-child{border-bottom:none}
.stat__value{font-size:17.5px;font-weight:700;line-height:19px}
.stat__label{font-size:5.4px;font-weight:500;margin-top:2px}
.ops{position:absolute;left:33px;top:91px}
.ops h2{font-size:14px;font-weight:700;line-height:17.5px;letter-spacing:.3px}
.ops h3{margin-top:5px;font-size:11px;font-weight:700;border-left:1.5px solid var(--navy);padding-left:5px;line-height:12px}
.ops .checks{margin-top:3px;margin-left:6px}
.ops .checks li{font-size:5.9px;line-height:9.7px}
.promise{position:absolute;left:34px;top:213px;width:162px;height:70px;border-radius:11px;background:var(--mist);padding:6px 10px;color:var(--band);font-weight:700;font-size:10.6px;line-height:15.3px}
.headline{position:absolute;left:36px;top:310px;font-size:15.8px;font-weight:800;line-height:20px;color:var(--band);letter-spacing:.2px}
.desc{position:absolute;left:36px;top:352px;width:350px;font-size:5.5px;line-height:7.5px;font-weight:500}
.photo--ops{left:37px;top:403px;width:180px;height:112px;background:linear-gradient(135deg,#1b2a3c,#3d5f7a 55%,#132030)}
.features{position:absolute;left:236px;top:425px;width:179px;list-style:none}
.features li{font-size:6px;font-weight:700;color:var(--navy);padding:4.5px 0;border-bottom:.6px solid #d5dbe4}
.features li:last-child{border-bottom:none}
.footer{position:absolute;left:0;top:529px;width:415px;height:56px;background:var(--tan);display:flex;align-items:center;justify-content:center;font-size:21.5px;font-weight:500;color:var(--ink)}
</style>
</head>
<body>

<section class="sheet sheet--front">
  <div class="brand"><span class="brand__dot"></span><span class="brand__name">HARBOR LEDGER<br>ADVISORS</span><span class="brand__tag">WHERE PROCESS MEETS PRECISION</span></div>
  <div class="url-pill">www.harborledger.com</div>
  <div class="photo photo--building" role="img" aria-label="Upward view of an ornate stone office building facade"></div>
  <div class="title-band"><h1>MASTER SERVICING<br>&amp; PORTFOLIO<br>OPTIMIZATION</h1></div>
  <p class="subtitle">End-to-End Post Default Management Strategy,<br>Recovery &amp; Compliance</p>
  <p class="intro">HLA delivers master servicing solutions powered by proprietary technology and automation. We centralize back-office operations, optimize recovery performance, and embed compliance controls across the full post-default lifecycle, reducing client overhead while increasing transparency and results.</p>
  <div class="col col--left">
    <h2>Strategy &amp; Recovery<br>Optimization</h2>
    <ul class="checks">
      <li>Recovery &amp; Liquidation Optimization</li>
      <li>Settlement Campaigns</li>
      <li>Payer Base Development &amp; Retention</li>
      <li>Penetration &amp; Conversion Tracking</li>
      <li>Omni-Channel &amp; Champion Challenger<br>Collection Strategy</li>
    </ul>
  </div>
  <div class="col col--right">
    <h2>Compliance &amp;<br>Risk Oversight</h2>
    <ul class="checks checks--tight">
      <li>Collection Agency Oversight</li>
      <li>Regulatory Compliance Audits (FDCPA, FCRA, UDAAP)</li>
      <li>SOL Calculation &amp; Tracking</li>
      <li>Reg F Balance Reconciliations</li>
      <li>Bankruptcy, Military &amp; Deceased Checks</li>
      <li>Complaint Management &amp; Monitoring</li>
    </ul>
  </div>
</section>

<section class="sheet sheet--back">
  <div class="brand"><span class="brand__dot"></span><span class="brand__name">HARBOR LEDGER<br>ADVISORS</span><span class="brand__tag">WHERE PROCESS MEETS PRECISION</span></div>
  <aside class="snapshot">
    <h3>PERFORMANCE<br>SNAPSHOT</h3>
    <div class="stat"><div class="stat__value">$155+ Million</div><div class="stat__label">Portfolio Collections Administered</div></div>
    <div class="stat"><div class="stat__value">573,000+</div><div class="stat__label">Defaulted Accounts Managed</div></div>
    <div class="stat"><div class="stat__value">3,700+</div><div class="stat__label">Compliance Audits Conducted</div></div>
    <div class="stat"><div class="stat__value">21%</div><div class="stat__label">3-Year Gross Collection Curve</div></div>
  </aside>
  <div class="ops">
    <h2>OPERATIONS<br>&amp; PORTFOLIO</h2>
    <h3>Management</h3>
    <ul class="checks">
      <li>Rigorous Placement &amp; Recall Processing</li>
      <li>Daily Balance Calculations &amp; Data Management</li>
      <li>Bank &amp; Inventory Reconciliation</li>
      <li>Portfolio Database Access</li>
      <li>Executive Reporting</li>
      <li>Bankruptcy Monitoring &amp; Support</li>
    </ul>
  </div>
  <div class="promise">Optimized Recoveries<br>Proven Scale Embedded<br>Compliance Measurable<br>Outcomes</div>
  <h2 class="headline">THE INTELLIGENCE BEHIND<br>EVERY COMPLIANT COMMAND</h2>
  <p class="desc">Description: LedgerView is HLA's compliance-led portfolio command intelligence platform — where regulatory authority and operational execution are unified under a single, AI-powered command center. Its live dashboard gives institutional clients total command over the post-default lifecycle: real-time compliance audit status across 15+ regulatory frameworks, centralized asset inventory with account-level drill-down, and automated workflow execution for placements, recalls, reconciliations, and recovery campaigns. LedgerView doesn't just display intelligence — it commands with it.</p>
  <div class="photo photo--ops" role="img" aria-label="Operator at a command desk with multiple monitoring screens"></div>
  <ul class="features">
    <li>Built-In Compliance Controls</li>
    <li>Centralized Asset Visibility</li>
    <li>Automated Workflow &amp; Recovery Execution</li>
    <li>Your Trusted Advisor.</li>
  </ul>
  <div class="footer">www.harborledger.com</div>
</section>

</body>
</html>
```